I need to refresh my meeting minutes pages (2 of them)

I have 2 pages that need to be modernized with a new look and feel. I have attached the 2 pages that need the refresh. I am okay with one page submissions as long as the winner is willing to add the second page before payment :-) Any questions please let me know. The logo on the page is not ours but a sample of what client may give us.

```html
<!DOCTYPE html>
<html lang="en">
<head>
<meta charset="utf-8">
<title>NVSD Meetings</title>
<link href="https://fonts.googleapis.com/css2?family=Kanit:wght@500;600&family=Kumbh+Sans:wght@400;500;600&display=swap" rel="stylesheet">
<style>
:root{
  --green:#066b2b;
  --ink:#2b2b2b;
  --grey-bg:#f3f4f5;
  --line:#d4d6d8;
  --star:#b9b9b9;
  --nav-dark:#333a40;
}
*{box-sizing:border-box;margin:0;padding:0}
html,body{width:1200px;height:766px;overflow:hidden}
body{position:relative;font-family:"Kumbh Sans",sans-serif;color:var(--ink);background:var(--grey-bg)}
.abs{position:absolute}
.header{position:absolute;left:0;top:0;width:1200px;height:103px;background:#fff;border-top:2px solid var(--green)}
.brand{position:absolute;left:40px;top:24px;font-family:"Kumbh Sans",sans-serif;font-weight:600;font-size:48px;line-height:56px;color:var(--green)}
.account-tab{position:absolute;left:880px;top:0;width:280px;height:36px;background:var(--green);border-radius:0 0 26px 26px;display:flex;align-items:center;justify-content:center;gap:16px;color:#fff;font-size:12px;font-weight:600}
.account-tab span{display:flex;align-items:center;gap:6px}
.account-tab .sep{width:1px;height:20px;background:#8fc0a0}
.nav a{position:absolute;top:56px;font-family:"Kanit",sans-serif;font-weight:500;font-size:14px;color:var(--ink);text-decoration:none;letter-spacing:.3px}
.nav a.active{color:var(--green);border-bottom:1px solid var(--green);padding:0 2px 1px}
.welcome{left:42px;top:131px;font-family:"Kanit",sans-serif;font-weight:600;font-size:20px;color:var(--green)}
.sidebar{left:40px;top:169px;width:326px;height:506px;background:#fff;border:1px solid var(--line)}
.side-row{position:absolute;left:0;width:100%;display:flex;align-items:center;padding:0 10px}
.side-row .label{margin-left:10px;font-size:18px;flex:1}
.side-row .toggle{font-size:20px;font-weight:600}
.featured-row{top:0;height:49px;border-bottom:1px solid var(--line)}
.year-row{top:58px;height:28px;color:var(--green)}
.meeting-list{position:absolute;left:68px;top:88px;list-style:none}
.meeting-list li{position:relative;height:45px;font-size:12.5px;line-height:19px;color:var(--ink)}
.meeting-list li .date{display:block}
.meeting-list li svg{position:absolute;left:-24px;top:3px}
.meeting-list li.current{color:var(--green)}
.meeting-list li.bold{font-weight:600}
.scroll-track{position:absolute;left:306px;top:90px;width:5px;height:396px;background:#eee}
.scroll-thumb{position:absolute;left:306px;top:90px;width:5px;height:324px;background:#cfcfcf}
.pager{top:128px;width:28px;height:32px;display:flex;align-items:center;justify-content:center}
.search-box{left:526px;top:128px;width:508px;height:32px;background:#fff;border:1px solid var(--line);font-size:12.5px;padding:0 8px;display:flex;align-items:center;justify-content:space-between;color:#333}
.search-btn{left:1042px;top:128px;width:119px;height:32px;background:var(--green);color:#fff;font-size:15px;font-weight:500;display:flex;align-items:center;justify-content:center;border-radius:2px}
.detail{left:400px;top:169px;width:760px;height:506px;background:#fff;border:1px solid var(--line)}
.detail .title{position:absolute;left:23px;top:18px;font-family:"Kanit",sans-serif;font-weight:600;font-size:17px;color:var(--green)}
.detail .date{position:absolute;left:24px;top:45px;font-size:15px}
.rule{position:absolute;left:24px;width:712px;height:1px;background:#ccc}
.venue{position:absolute;left:24px;top:91px;font-family:"Kanit",sans-serif;font-weight:600;font-size:14px;color:var(--green)}
.addr{position:absolute;left:24px;top:118px;font-size:15px;line-height:23px}
.addr div{display:flex;align-items:center;gap:8px}
.addr .ind{padding-left:24px}
.desc{position:absolute;left:24px;top:207px;width:640px;font-size:15px;line-height:23px}
.actions{position:absolute;left:24px;top:435px;display:flex;gap:16px}
.action{width:134px;height:44px;border:1px solid #ccc;background:#fff;display:flex;align-items:center;gap:8px;padding-left:14px;font-size:10.5px;line-height:12px;white-space:nowrap}
.footer{position:absolute;left:0;top:718px;width:1200px;height:48px;background:var(--green);color:#fff;display:flex;align-items:center;justify-content:space-between;padding:0 41px 0 42px}
.footer .copy{font-family:"Kanit",sans-serif;font-weight:500;font-size:16px}
.footer .mark{font-family:"Kanit",sans-serif;font-weight:500;font-size:22px}
</style>
</head>
<body>
<header class="header">
  <div class="brand">NVSD</div>
  <div class="account-tab">
    <span><svg width="12" height="13" viewBox="0 0 12 13" fill="none" stroke="#fff" stroke-width="1.5"><rect x="1" y="1" width="7" height="11"/><path d="M5 6.5h6M9 4.5l2 2-2 2"/></svg>Sign Out</span>
    <span class="sep"></span>
    <span><svg width="13" height="14" viewBox="0 0 13 14" fill="#fff"><circle cx="6.5" cy="3.5" r="3"/><path d="M0 14v-4q0-3 4-3h5q4 0 4 3v4z"/></svg>Alan Mercer</span>
  </div>
  <nav class="nav">
    <a style="left:798px">Featured</a>
    <a class="active" style="left:902px">Meetings</a>
    <a style="left:1010px">Agenda</a>
    <a style="left:1109px">Policies</a>
  </nav>
</header>

<h1 class="abs welcome">Welcome to NVSD</h1>

<aside class="abs sidebar">
  <div class="side-row featured-row">
    <svg width="24" height="22" viewBox="0 0 24 22" fill="none" stroke="#444" stroke-width="1.2"><rect x="1" y="1" width="22" height="20"/><circle cx="12" cy="11" r="3"/><circle cx="12" cy="11" r="6" stroke-dasharray="3 2"/></svg>
    <span class="label">Featured</span><span class="toggle">+</span>
  </div>
  <div class="side-row year-row">
    <svg width="24" height="24" viewBox="0 0 24 24" fill="none" stroke="var(--green)" stroke-width="1.2"><rect x="1" y="3" width="22" height="19"/><path d="M1 8h22M6 1v4M18 1v4"/><text x="5" y="18" font-size="6" fill="var(--green)" stroke="none">365</text></svg>
    <span class="label">2015</span><span class="toggle">–</span>
  </div>
  <ul class="meeting-list">
    <li class="current"><svg width="14" height="14" viewBox="0 0 24 24" fill="var(--green)"><path d="M12 1l3.4 7 7.6 1-5.5 5.3 1.3 7.7L12 18.3 5.2 22l1.3-7.7L1 9l7.6-1z"/></svg><span class="date">May 1, 2025 (Thu)</span>Special Meeting Agenda</li>
    <li><svg width="14" height="14" viewBox="0 0 24 24" fill="var(--star)"><path d="M12 1l3.4 7 7.6 1-5.5 5.3 1.3 7.7L12 18.3 5.2 22l1.3-7.7L1 9l7.6-1z"/></svg><span class="date">May 1, 2025 (Thu)</span>Special Meeting Agenda</li>
    <li><svg width="14" height="14" viewBox="0 0 24 24" fill="var(--star)"><path d="M12 1l3.4 7 7.6 1-5.5 5.3 1.3 7.7L12 18.3 5.2 22l1.3-7.7L1 9l7.6-1z"/></svg><span class="date">May 1, 2025 (Thu)</span>Special Meeting Agenda</li>
    <li><svg width="14" height="14" viewBox="0 0 24 24" fill="var(--star)"><path d="M12 1l3.4 7 7.6 1-5.5 5.3 1.3 7.7L12 18.3 5.2 22l1.3-7.7L1 9l7.6-1z"/></svg><span class="date">May 1, 2025 (Thu)</span>Special Meeting Agenda</li>
    <li><svg width="14" height="14" viewBox="0 0 24 24" fill="var(--star)"><path d="M12 1l3.4 7 7.6 1-5.5 5.3 1.3 7.7L12 18.3 5.2 22l1.3-7.7L1 9l7.6-1z"/></svg><span class="date">May 1, 2025 (Thu)</span>Special Meeting Agenda</li>
    <li><svg width="14" height="14" viewBox="0 0 24 24" fill="var(--star)"><path d="M12 1l3.4 7 7.6 1-5.5 5.3 1.3 7.7L12 18.3 5.2 22l1.3-7.7L1 9l7.6-1z"/></svg><span class="date">May 1, 2025 (Thu)</span>Special Meeting Agenda</li>
    <li class="bold"><svg width="14" height="14" viewBox="0 0 24 24" fill="var(--star)"><path d="M12 1l3.4 7 7.6 1-5.5 5.3 1.3 7.7L12 18.3 5.2 22l1.3-7.7L1 9l7.6-1z"/></svg><span class="date">May 1, 2025 (Thu)</span>Special Meeting Agenda</li>
    <li class="bold"><svg width="14" height="14" viewBox="0 0 24 24" fill="var(--star)"><path d="M12 1l3.4 7 7.6 1-5.5 5.3 1.3 7.7L12 18.3 5.2 22l1.3-7.7L1 9l7.6-1z"/></svg><span class="date">May 1, 2025 (Thu)</span>Special Meeting Agenda</li>
    <li><svg width="14" height="14" viewBox="0 0 24 24" fill="var(--star)"><path d="M12 1l3.4 7 7.6 1-5.5 5.3 1.3 7.7L12 18.3 5.2 22l1.3-7.7L1 9l7.6-1z"/></svg><span class="date">May 1, 2025 (Thu)</span>Special Meeting Agenda</li>
  </ul>
  <div class="scroll-track"></div>
  <div class="scroll-thumb"></div>
</aside>

<div class="abs pager" style="left:401px;background:var(--nav-dark)"><svg width="10" height="14" viewBox="0 0 10 14" fill="none" stroke="#fff" stroke-width="2.5"><path d="M8 1L2 7l6 6"/></svg></div>
<div class="abs pager" style="left:437px;background:var(--green)"><svg width="10" height="14" viewBox="0 0 10 14" fill="none" stroke="#fff" stroke-width="2.5"><path d="M2 1l6 6-6 6"/></svg></div>
<div class="abs search-box"><span>search meetings</span><svg width="16" height="16" viewBox="0 0 16 16" fill="none" stroke="#999" stroke-width="1.5"><circle cx="8" cy="8" r="6.5"/></svg></div>
<div class="abs search-btn">Search</div>

<main class="abs detail">
  <h2 class="title">Regular Meeting Agenda</h2>
  <div class="date">Thursday, April 24, 2025</div>
  <div class="rule" style="top:77px"></div>
  <div class="venue">Lakeview High School Media Center</div>
  <div class="addr">
    <div><svg width="16" height="18" viewBox="0 0 16 18" fill="none" stroke="#333" stroke-width="1.3"><path d="M8 17s-6-6-6-10a6 6 0 0 1 12 0c0 4-6 10-6 10z"/><circle cx="8" cy="7" r="2.2"/></svg>1800 North Maple Grove Road</div>
    <div class="ind">Fairview, Ohio 44100</div>
    <div><svg width="16" height="16" viewBox="0 0 16 16" fill="none" stroke="#333" stroke-width="1.3"><circle cx="8" cy="8" r="7" stroke-dasharray="9 2"/><path d="M8 3v5h4"/></svg>06:00 pm</div>
  </div>
  <div class="rule" style="top:197px"></div>
  <p class="desc">This meeting is a meeting of the Board of Education in public for the purpose of conducting the District’s business. There is a time for public participation durin View the Agenda</p>
  <div class="actions">
    <div class="action"><svg width="28" height="32" viewBox="0 0 28 32" fill="none" stroke="var(--green)" stroke-width="1.6"><path d="M2 1h18l6 6v24H2z"/><path d="M6 10h2M11 10h11M6 15h2M11 15h11M6 20h2M11 20h11M6 25h2M11 25h11"/></svg><span>View<br>the Agenda</span></div>
    <div class="action"><svg width="30" height="32" viewBox="0 0 30 32" fill="none" stroke="var(--green)" stroke-width="1.6"><path d="M4 1h16l6 6v24H4z"/><rect x="1" y="12" width="28" height="11" fill="var(--green)"/><text x="3" y="21.5" font-size="9.5" font-weight="700" fill="#fff" stroke="none" font-family="sans-serif">PDF</text></svg><span>Download<br>Agenda as PDF</span></div>
    <div class="action"><svg width="32" height="32" viewBox="0 0 32 32" fill="none" stroke="var(--green)" stroke-width="1.6"><rect x="8" y="1" width="16" height="9"/><rect x="1" y="10" width="30" height="14" rx="2"/><rect x="8" y="18" width="16" height="13"/><path d="M11 23h10M11 27h10"/></svg><span>Print<br>the Agenda</span></div>
    <div class="action"><svg width="40" height="32" viewBox="0 0 40 32" fill="none" stroke="var(--green)" stroke-width="1.6"><circle cx="7" cy="17" r="5"/><circle cx="31" cy="6" r="5"/><circle cx="31" cy="27" r="5"/><path d="M11.5 14.5l15-6M11.5 19.5l15 5"/></svg><span>Share<br>this Page</span></div>
  </div>
</main>

<footer class="footer">
  <span class="copy">@ 2015 NVSD. All Rights Reserved</span>
  <span class="mark">NVSD</span>
</footer>
</body>
</html>
```